Create a powerful circular diagram to get the message accross

I need a diagram designed that demonstrates the power of our service by showing the limitations of all our competitors. All the data is provided it just needs to be illustrated.

Target Market(s)

People who work in all the categories listed, we are trying to show them why Open Path Renewal is better than the rest

Font styles to use
Sans Serif

Requirements
Must have
• You need to create one big wheel that groups together all the of the modailties listed according to their colors. So for example you can have all the modalities that only have the red color underneath and put them all under one group. Some modalities have two or three colors you can only group them with modlities with the exact same number of colors and type of colors. The idea is to show that Open Path renewal is the only modality that covers all color fields (ie: color catagories of physical, mental, emotional etc.
• It must have te OPR logo and the lumawell ventures logo on it
• it must have the web address
• www.lumawell-example.com.au on it
• you cannot leave anything out all modalities and fields must be included.
• Must match the Lumawell Blue and the lumawell font
Nice to have
• i would love to see you use your creativity :)
Should not have
• Limit the amount of black, have a look at www.lumawell-example.com.au for brand colors

```html
<!DOCTYPE html>
<html lang="en">
<head>
<meta charset="utf-8">
<title>Open Path Renewal – Healing on All Levels</title>
<link href="https://fonts.googleapis.com/css2?family=Noto+Serif:ital,wght@1,700&family=Poppins:ital,wght@0,400;0,500;0,600;0,700;1,400;1,500;1,600&display=swap" rel="stylesheet">
<style>
  :root {
    --brand: #0a89cf;
    --brand-text: #1a8fd2;
    --ink: #1f1f1f;
    --white: #ffffff;
    --physical: #ec1c2d;
    --mental: #00ade0;
    --emotional: #3ab54a;
    --energetic: #f47b20;
    --subconscious: #eab520;
    --spiritual: #7d52a0;
    --testing: #d4489a;
  }
  html, body { margin: 0; padding: 0; overflow: hidden; background: var(--white); }
  .canvas {
    position: relative;
    width: 1200px;
    height: 733px;
    overflow: hidden;
    background: var(--brand);
    font-family: "Poppins", sans-serif;
  }
  .sheet {
    position: absolute;
    left: 17px; top: 17px; right: 17px; bottom: 16px;
    background: var(--white);
  }
  .brand-mark {
    position: absolute;
    left: 52px; top: 35px;
    display: flex; align-items: center; gap: 12px;
  }
  .brand-mark__dot {
    width: 64px; height: 64px;
    border: 2px solid var(--brand-text);
    border-radius: 50%;
    box-sizing: border-box;
  }
  .brand-mark__name {
    font-size: 28px; font-weight: 500; color: var(--brand-text);
    line-height: 1;
  }
  .web-pill {
    position: absolute;
    left: 449px; top: 43px;
    width: 314px; height: 45px;
    box-sizing: border-box;
    border: 1.5px solid var(--brand-text);
    border-radius: 23px;
    display: flex; align-items: center; justify-content: center;
    font-family: "Noto Serif", serif;
    font-style: italic; font-weight: 700;
    font-size: 18px; color: var(--brand);
  }
  .partner-mark {
    position: absolute;
    right: 62px; top: 42px;
    text-align: right;
    color: var(--brand-text);
    font-weight: 400;
    line-height: 1;
  }
  .partner-mark__main { font-size: 34px; display: block; }
  .partner-mark__sub { font-size: 10px; letter-spacing: 4px; display: block; margin-top: 2px; }
  .intro {
    position: absolute;
    left: 59px; top: 152px;
    width: 490px;
    margin: 0;
    font-size: 14.3px; line-height: 17.8px;
    letter-spacing: -0.15px;
    color: var(--brand-text);
  }
  .intro p { margin: 0 0 2px; }
  .claims {
    position: absolute;
    left: 29px; top: 255px;
    width: 522px; height: 112px;
    box-sizing: border-box;
    background: var(--brand);
    border-radius: 28px;
    padding: 15px 10px 0 30px;
    margin: 0;
    list-style: none;
    color: var(--white);
    font-size: 14.3px; font-weight: 500; line-height: 17.8px;
    letter-spacing: -0.2px;
  }
  .claims li { position: relative; margin-bottom: 8px; }
  .claims li::before {
    content: "";
    position: absolute;
    left: -18px; top: 6px;
    width: 6px; height: 6px;
    background: var(--white);
    transform: rotate(45deg);
  }
  .levels {
    position: absolute;
    left: 59px; top: 382px;
    width: 475px;
    margin: 0;
    font-size: 13.2px; line-height: 15px; font-style: italic;
    letter-spacing: -0.2px;
  }
  .levels dt { font-weight: 600; color: var(--ink); margin-top: 6px; }
  .levels dt:first-child { margin-top: 0; }
  .levels dd { margin: 0; color: var(--brand-text); font-weight: 500; }
  .wheel {
    position: absolute;
    left: 571px; top: 93px;
    width: 590px; height: 590px;
  }
  .wheel .slice { stroke: var(--white); stroke-width: 5; }
  .wedge-outline { fill: none; stroke: var(--white); stroke-width: 4; }
  .ring-label { fill: var(--white); font-weight: 600; font-size: 21px; letter-spacing: 1px; }
  .ring-label--small { font-size: 14px; letter-spacing: 0.5px; }
  .ring-label--mid { font-size: 18px; }
  .group-names { fill: var(--white); font-weight: 600; font-size: 9px; text-anchor: middle; }
  .hub-band { fill: none; stroke-width: 8; }
  .hub-name { fill: var(--brand-text); font-weight: 500; font-size: 56px; text-anchor: middle; }
</style>
</head>
<body>
<div class="canvas">
  <div class="sheet"></div>

  <div class="brand-mark">
    <span class="brand-mark__dot"></span>
    <span class="brand-mark__name">Open Path Renewal</span>
  </div>

  <div class="web-pill">www.lumawell-example.com.au</div>

  <div class="partner-mark">
    <span class="partner-mark__main">lumawell</span>
    <span class="partner-mark__sub">ventures</span>
  </div>

  <div class="intro">
    <p>The client must experience healing on all levels</p>
    <p>IE: when you see a phychic they are using their intiutive abilities but you are not for the client to be empowered and heal themselves they must be able to access their own subconsious not have it done externally</p>
  </div>

  <ul class="claims">
    <li>OPR is the only modality that incorporates emotional processing in the body for a whole of self healing</li>
    <li>OPR is the only modality that empowers the client to heal on all levels simultaneously</li>
  </ul>

  <dl class="levels">
    <dt>PHYISICAL</dt>
    <dd>the clients must have a physcal experience</dd>
    <dt>EMOTIONAL</dt>
    <dd>emotions must be explored &amp; experienced by the client and measured for best results</dd>
    <dt>ENERGETIC</dt>
    <dd>the client must have an experience of feeling and directing energy in their own bodies by themselves</dd>
    <dt>SUBCONSCIOUS</dt>
    <dd>the client must access their own subconsious during the session</dd>
    <dt>SPIRITUAL /SUPER CONSIOUS</dt>
    <dd>the client must experience their higher self or: wisdom/ephiany from within during the session</dd>
    <dt>BEFORE &amp; AFTER TESTING</dt>
    <dd>the before and after results must be provided by the client, documented and analysed by the client and the practitioner.</dd>
  </dl>

  <svg class="wheel" viewBox="-295 -295 590 590" role="img" aria-label="Modalities grouped by the healing levels they cover, with OPR covering every level">
    <defs>
      <path id="arc-physical" d="M -105.7 -237.5 A 260 260 0 0 1 105.7 -237.5"/>
      <path id="arc-mental" d="M 105.7 -237.5 A 260 260 0 0 1 254.3 -54.1"/>
      <path id="arc-testing-outer" d="M -264.1 -56.1 A 270 270 0 0 1 -109.8 -246.7"/>
      <path id="arc-testing-inner" d="M -247.5 -52.6 A 253 253 0 0 1 -102.9 -231.1"/>
      <path id="arc-emotional" d="M 220.6 172.4 A 280 280 0 0 0 273.9 -58.2"/>
      <path id="arc-energetic" d="M 0 280 A 280 280 0 0 0 220.6 172.4"/>
      <path id="arc-subconscious" d="M -217.6 176.2 A 280 280 0 0 0 0 280"/>
      <path id="arc-spiritual-outer" d="M -279.7 -59.5 A 286 286 0 0 0 -222.3 180.0"/>
      <path id="arc-spiritual-inner" d="M -262.1 -55.7 A 268 268 0 0 0 -208.3 168.7"/>

      <path id="band-full" d="M -54.7 -239.8 A 246 246 0 0 1 54.7 -239.8 L 23.1 -101.4 A 104 104 0 0 0 -23.1 -101.4 Z"/>
      <path id="band-half" d="M -27.54 -244.45 A 246 246 0 0 1 27.54 -244.45 L 11.64 -103.35 A 104 104 0 0 0 -11.64 -103.35 Z"/>
      <path id="band-third" d="M -18.38 -245.31 A 246 246 0 0 1 18.38 -245.31 L 7.77 -103.71 A 104 104 0 0 0 -7.77 -103.71 Z"/>
      <path id="band-quarter" d="M -13.79 -245.61 A 246 246 0 0 1 13.79 -245.61 L 5.83 -103.84 A 104 104 0 0 0 -5.83 -103.84 Z"/>
    </defs>

    <g class="level-ring">
      <path class="slice" fill="var(--physical)" d="M0 0 L -118.4 -265.8 A 291 291 0 0 1 118.4 -265.8 Z"/>
      <path class="slice" fill="var(--mental)" d="M0 0 L 118.4 -265.8 A 291 291 0 0 1 284.6 -60.5 Z"/>
      <path class="slice" fill="var(--emotional)" d="M0 0 L 284.6 -60.5 A 291 291 0 0 1 229.3 179.2 Z"/>
      <path class="slice" fill="var(--energetic)" d="M0 0 L 229.3 179.2 A 291 291 0 0 1 0 291 Z"/>
      <path class="slice" fill="var(--subconscious)" d="M0 0 L 0 291 A 291 291 0 0 1 -226.1 183.1 Z"/>
      <path class="slice" fill="var(--spiritual)" d="M0 0 L -226.1 183.1 A 291 291 0 0 1 -284.6 -60.5 Z"/>
      <path class="slice" fill="var(--testing)" d="M0 0 L -284.6 -60.5 A 291 291 0 0 1 -118.4 -265.8 Z"/>
    </g>

    <g class="ring-labels">
      <text class="ring-label"><textPath href="#arc-physical" startOffset="50%" text-anchor="middle">PHYSICAL</textPath></text>
      <text class="ring-label ring-label--mid"><textPath href="#arc-mental" startOffset="50%" text-anchor="middle">MENTAL/CONSIOUS</textPath></text>
      <text class="ring-label ring-label--small"><textPath href="#arc-testing-outer" startOffset="50%" text-anchor="middle">BEFORE &amp; AFTER</textPath></text>
      <text class="ring-label ring-label--small"><textPath href="#arc-testing-inner" startOffset="62%" text-anchor="middle">TESTING</textPath></text>
      <text class="ring-label"><textPath href="#arc-emotional" startOffset="50%" text-anchor="middle">EMOTIONAL</textPath></text>
      <text class="ring-label"><textPath href="#arc-energetic" startOffset="50%" text-anchor="middle">ENERGETIC</textPath></text>
      <text class="ring-label ring-label--mid"><textPath href="#arc-subconscious" startOffset="50%" text-anchor="middle">SUBCONSCIOUS</textPath></text>
      <text class="ring-label ring-label--small"><textPath href="#arc-spiritual-outer" startOffset="50%" text-anchor="middle">SUPERCONSCIOUS</textPath></text>
      <text class="ring-label ring-label--small"><textPath href="#arc-spiritual-inner" startOffset="50%" text-anchor="middle">SPIRITUAL/</textPath></text>
    </g>

    <circle cx="0" cy="0" r="250" fill="var(--white)"/>

    <!-- modality groups: each band is split into the exact levels it covers -->
    <g class="group group--physical" transform="rotate(12.857)">
      <use href="#band-full" fill="var(--physical)"/>
      <use href="#band-full" class="wedge-outline"/>
    </g>
    <g class="group group--physical-mental" transform="rotate(38.571)">
      <use href="#band-half" transform="rotate(-6.4286)" fill="var(--physical)"/>
      <use href="#band-half" transform="rotate(6.4286)" fill="var(--mental)"/>
      <use href="#band-full" class="wedge-outline"/>
    </g>
    <g class="group group--mental" transform="rotate(64.286)">
      <use href="#band-full" fill="var(--mental)"/>
      <use href="#band-full" class="wedge-outline"/>
    </g>
    <g class="group group--mental-subconscious" transform="rotate(90)">
      <use href="#band-half" transform="rotate(-6.4286)" fill="var(--mental)"/>
      <use href="#band-half" transform="rotate(6.4286)" fill="var(--subconscious)"/>
      <use href="#band-full" class="wedge-outline"/>
    </g>
    <g class="group group--mental-subconscious-testing" transform="rotate(115.714)">
      <use href="#band-third" transform="rotate(-8.5714)" fill="var(--mental)"/>
      <use href="#band-third" fill="var(--subconscious)"/>
      <use href="#band-third" transform="rotate(8.5714)" fill="var(--testing)"/>
      <use href="#band-full" class="wedge-outline"/>
    </g>
    <g class="group group--physical-mental-subconscious-testing" transform="rotate(141.429)">
      <use href="#band-quarter" transform="rotate(-9.6429)" fill="var(--physical)"/>
      <use href="#band-quarter" transform="rotate(-3.2143)" fill="var(--mental)"/>
      <use href="#band-quarter" transform="rotate(3.2143)" fill="var(--subconscious)"/>
      <use href="#band-quarter" transform="rotate(9.6429)" fill="var(--testing)"/>
      <use href="#band-full" class="wedge-outline"/>
    </g>
    <g class="group group--physical-subconscious-testing" transform="rotate(167.143)">
      <use href="#band-third" transform="rotate(-8.5714)" fill="var(--physical)"/>
      <use href="#band-third" fill="var(--subconscious)"/>
      <use href="#band-third" transform="rotate(8.5714)" fill="var(--testing)"/>
      <use href="#band-full" class="wedge-outline"/>
    </g>
    <g class="group group--subconscious-spiritual" transform="rotate(192.857)">
      <use href="#band-half" transform="rotate(-6.4286)" fill="var(--subconscious)"/>
      <use href="#band-half" transform="rotate(6.4286)" fill="var(--spiritual)"/>
      <use href="#band-full" class="wedge-outline"/>
    </g>
    <g class="group group--physical-testing" transform="rotate(218.571)">
      <use href="#band-half" transform="rotate(-6.4286)" fill="var(--physical)"/>
      <use href="#band-half" transform="rotate(6.4286)" fill="var(--testing)"/>
      <use href="#band-full" class="wedge-outline"/>
    </g>
    <g class="group group--energetic-testing" transform="rotate(244.286)">
      <use href="#band-half" transform="rotate(-6.4286)" fill="var(--energetic)"/>
      <use href="#band-half" transform="rotate(6.4286)" fill="var(--testing)"/>
      <use href="#band-full" class="wedge-outline"/>
    </g>
    <g class="group group--physical-energetic-testing" transform="rotate(270)">
      <use href="#band-third" transform="rotate(-8.5714)" fill="var(--physical)"/>
      <use href="#band-third" fill="var(--energetic)"/>
      <use href="#band-third" transform="rotate(8.5714)" fill="var(--testing)"/>
      <use href="#band-full" class="wedge-outline"/>
    </g>
    <g class="group group--energetic" transform="rotate(295.714)">
      <use href="#band-full" fill="var(--energetic)"/>
      <use href="#band-full" class="wedge-outline"/>
    </g>
    <g class="group group--physical-energetic" transform="rotate(321.429)">
      <use href="#band-half" transform="rotate(-6.4286)" fill="var(--physical)"/>
      <use href="#band-half" transform="rotate(6.4286)" fill="var(--energetic)"/>
      <use href="#band-full" class="wedge-outline"/>
    </g>
    <g class="group group--physical-mental-energetic" transform="rotate(347.143)">
      <use href="#band-third" transform="rotate(-8.5714)" fill="var(--physical)"/>
      <use href="#band-third" fill="var(--mental)"/>
      <use href="#band-third" transform="rotate(8.5714)" fill="var(--energetic)"/>
      <use href="#band-full" class="wedge-outline"/>
    </g>

    <!-- group names, read outward on the right half and inward on the left half -->
    <g class="group-names">
      <text transform="rotate(-77.143)">
        <tspan x="178" y="-13">MASSAGE / YOGA</tspan>
        <tspan x="178" y="-2.5">NATROPATHY</tspan>
        <tspan x="178" y="8">AYURVEDIC MEDICINE</tspan>
        <tspan x="178" y="18.5">WESTERN MEDICINE</tspan>
      </text>
      <text transform="rotate(-51.429)"><tspan x="178" y="3">PSYCHIC INTUITIVE</tspan></text>
      <text transform="rotate(-25.714)">
        <tspan x="178" y="-13">PSHYCHOLOGY</tspan>
        <tspan x="178" y="-2.5">LIFE COACHING</tspan>
        <tspan x="178" y="8">MINDFULLNESS</tspan>
        <tspan x="178" y="18.5">MEDITATION</tspan>
      </text>
      <text transform="rotate(0)">
        <tspan x="178" y="-2">HYPNO-THERAPY</tspan>
        <tspan x="178" y="8.5">INNER CHILD HEALING</tspan>
      </text>
      <text transform="rotate(25.714)">
        <tspan x="178" y="-2">NLP</tspan>
        <tspan x="178" y="8.5">TIMELINE THERAPY</tspan>
      </text>
      <text transform="rotate(51.429)"><tspan x="178" y="3">EFT</tspan></text>
      <text transform="rotate(77.143)">
        <tspan x="178" y="-2">KINESIOLOGY</tspan>
        <tspan x="178" y="8.5">BOWEN THERAPY</tspan>
      </text>
      <text transform="rotate(282.857)"><tspan x="-178" y="3">THETA HEALING</tspan></text>
      <text transform="rotate(308.571)"><tspan x="-178" y="3">NUTRITIONAL HEALING</tspan></text>
      <text transform="rotate(334.286)"><tspan x="-178" y="3">ENERGY MEDICINE</tspan></text>
      <text transform="rotate(360)">
        <tspan x="-178" y="-2">CHINESE MEDICINE</tspan>
        <tspan x="-178" y="8.5">CHIRO-PRACTIC</tspan>
      </text>
      <text transform="rotate(385.714)">
        <tspan x="-178" y="-2">REIKI</tspan>
        <tspan x="-178" y="8.5">CRYSTAL HEALING</tspan>
      </text>
      <text transform="rotate(411.429)"><tspan x="-178" y="3">ACCUPUNC-TURE</tspan></text>
      <text transform="rotate(437.143)"><tspan x="-178" y="3">FAMILY-CONSTELLATION</tspan></text>
    </g>

    <!-- hub: OPR covers all seven levels -->
    <circle cx="0" cy="0" r="99" fill="var(--white)"/>
    <g class="hub-ring" transform="rotate(-115.714)">
      <circle class="hub-band" r="94" stroke="var(--physical)" stroke-dasharray="84.37 506.25" stroke-dashoffset="0"/>
      <circle class="hub-band" r="94" stroke="var(--mental)" stroke-dasharray="84.37 506.25" stroke-dashoffset="-84.37"/>
      <circle class="hub-band" r="94" stroke="var(--emotional)" stroke-dasharray="84.37 506.25" stroke-dashoffset="-168.74"/>
      <circle class="hub-band" r="94" stroke="var(--energetic)" stroke-dasharray="84.37 506.25" stroke-dashoffset="-253.11"/>
      <circle class="hub-band" r="94" stroke="var(--subconscious)" stroke-dasharray="84.37 506.25" stroke-dashoffset="-337.48"/>
      <circle class="hub-band" r="94" stroke="var(--spiritual)" stroke-dasharray="84.37 506.25" stroke-dashoffset="-421.85"/>
      <circle class="hub-band" r="94" stroke="var(--testing)" stroke-dasharray="84.37 506.25" stroke-dashoffset="-506.22"/>
    </g>
    <text class="hub-name" x="0" y="19">OPR</text>
  </svg>
</div>
</body>
</html>
```